Wedding Photographer needs a website update

Hi all,

I've had this website (http://tomasferreiraphoto.net) for a couple of years and, although I still like it, I feel it's time for a change.

I would like to refresh the web design, while keeping it "fresh", somehow minimalist and with an overall elegance. The main element should be the pictures.

Should you need to retouch/update (not drastically though) the logo in order to fit the new design, I'm up for suggestions.

Target Market(s)

Couples looking for a wedding photographer: age 20-40.

Industry/Entity Type

Wedding

Colors

Designer to choose colors to be used in the design.

Requirements
Nice to have
• Should follow the existing structure as a guideline.

```html
<!DOCTYPE html>
<html lang="en">
<head>
<meta charset="utf-8">
<title>Tomás Ferreira — Wedding Photography</title>
<link href="https://fonts.googleapis.com/css2?family=Open+Sans:ital,wght@0,300;0,400;1,400&family=Vollkorn:wght@400&display=swap" rel="stylesheet">
<style>
:root{
  --page:#f4f4f4;
  --panel:#ffffff;
  --text:#555555;
  --heading:#444444;
  --muted:#9a9a9a;
  --faint:#c8c8c8;
  --rule:#e4e4e4;
  --accent:#b0103a;
  --brand:#3c5467;
  --photo-warm:#e9d2bd;
}
*{box-sizing:border-box;margin:0;padding:0}
html,body{width:1200px;height:1008px;overflow:hidden}
body{background:var(--page);font-family:"Open Sans",Arial,sans-serif;color:var(--text);position:relative}

.social{position:absolute;display:flex;gap:18px;align-items:center}
.social span{width:9px;height:9px;border-radius:50%;background:var(--faint);display:block}
.social--top{top:14px;left:968px}
.social--foot{top:988px;left:993px;gap:20px}
.search{position:absolute;top:11px;left:1152px}

.brand{position:absolute;top:5px;left:0;width:1200px;text-align:center}
.brand__mark{width:79px;height:88px;margin:0 auto;background:linear-gradient(180deg,#6a8396,var(--brand))}
.brand__name{font-family:"Vollkorn",Georgia,serif;font-size:24px;letter-spacing:1px;color:#2a2418;margin-top:4px;line-height:30px}
.brand__tag{font-size:7px;letter-spacing:2.5px;color:var(--brand);line-height:10px}

.rule{position:absolute;left:20px;width:1160px;height:1px;background:var(--rule)}

.nav{position:absolute;top:163px;left:0;width:1200px;display:flex;justify-content:center;gap:23px;font-size:14px;color:var(--muted);text-transform:uppercase}
.nav a{color:inherit;text-decoration:none;display:flex;align-items:center;gap:6px;padding-bottom:3px}
.nav a.is-current{border-bottom:1px solid #888;color:#888}
.nav svg{width:10px;height:6px}

.slider{position:absolute;top:210px;left:0;width:1200px;height:578px}
.slide__photo{position:absolute;left:70px;top:0;width:615px;height:578px;background:radial-gradient(circle at 60% 45%,#f1c7a8,#e6d5c6 55%,#f3eee9)}
.slide__next{position:absolute;left:1124px;top:0;width:76px;height:574px;background:linear-gradient(90deg,#ece3dc,#f1ebe6)}
.slide__card{position:absolute;left:685px;top:0;width:439px;height:578px;background:var(--panel)}
.dots{position:absolute;top:27px;left:123px;display:flex;gap:10px}
.dots span{width:10px;height:10px;border-radius:50%;border:1px solid #ddd}
.dots span.is-active{background:var(--accent);border-color:var(--accent)}
.card__date{position:absolute;top:78px;left:37px;font-size:10px;font-style:italic;color:var(--faint)}
.card__title{position:absolute;top:100px;left:37px;width:380px;font-family:"Vollkorn",Georgia,serif;font-weight:400;font-size:40px;line-height:42px;color:var(--heading);text-transform:uppercase}
.thumbs{position:absolute;top:259px;left:37px;display:flex;gap:9px}
.thumb{width:84px;height:84px}
.thumb--a{background:linear-gradient(180deg,#c9c2a2,#7e8f4b)}
.thumb--b{background:linear-gradient(135deg,#d8c3b2,#6d5f5a)}
.thumb--more{width:91px;border:1px solid #e6e6e6;display:flex;align-items:center;justify-content:center;color:#888;font-size:18px;letter-spacing:1px;margin-left:-7px}
.card__cat{position:absolute;top:372px;left:37px;font-size:13px;font-style:italic;color:var(--muted)}
.card__excerpt{position:absolute;top:409px;left:37px;width:360px;font-size:13px;line-height:20.5px;color:var(--text)}
.card__likes{position:absolute;top:530px;left:39px;display:flex;align-items:center;gap:7px;font-size:13px}
.arrow{position:absolute;top:465px}
.arrow--prev{left:10px}
.arrow--next{left:1160px}

.ctas{position:absolute;top:868px;left:0;width:1200px}
.cta{position:absolute;width:240px;margin-left:-120px;text-align:center}
.cta small{display:block;font-size:15px;font-style:italic;color:var(--muted);line-height:20px}
.cta strong{display:block;font-family:"Vollkorn",Georgia,serif;font-weight:400;font-size:26px;color:var(--heading);line-height:30px}

.copyright{position:absolute;top:983px;left:22px;font-size:14px;color:#555}
</style>
</head>
<body>
<div class="social social--top" aria-label="Social links"><span></span><span></span><span></span><span></span><span></span><span></span></div>
<svg class="search" width="16" height="16" viewBox="0 0 16 16" aria-label="Search"><circle cx="9" cy="7" r="5" fill="none" stroke="#b0103a" stroke-width="1.5"/><line x1="5.5" y1="10.5" x2="1.5" y2="14.5" stroke="#b0103a" stroke-width="1.5"/></svg>

<header class="brand">
  <div class="brand__mark"></div>
  <div class="brand__name">Tomás Ferreira</div>
  <div class="brand__tag">FOTOJORNALISTA</div>
</header>
<div class="rule" style="top:139px"></div>

<nav class="nav">
  <a class="is-current">Homepage <svg viewBox="0 0 10 6"><path d="M0 0 5 5 10 0" fill="none" stroke="currentColor"/></svg></a>
  <a>Blog</a>
  <a>Gallery posts <svg viewBox="0 0 10 6"><path d="M0 0 5 5 10 0" fill="none" stroke="currentColor"/></svg></a>
  <a>Blog posts <svg viewBox="0 0 10 6"><path d="M0 0 5 5 10 0" fill="none" stroke="currentColor"/></svg></a>
  <a>Availability calendar</a>
  <a>Contact</a>
</nav>

<section class="slider">
  <div class="slide__photo" role="img" aria-label="Close-up photo of a bride with flowers in her hair and the groom"></div>
  <div class="slide__next" role="img" aria-label="Next slide photo, soft wedding tones"></div>
  <article class="slide__card">
    <div class="dots"><span class="is-active"></span><span></span><span></span><span></span><span></span><span></span><span></span><span></span><span></span><span></span></div>
    <div class="card__date">07 December</div>
    <h2 class="card__title">Horizontal scroll gallery + video</h2>
    <div class="thumbs">
      <div class="thumb thumb--a" role="img" aria-label="Couple standing in a park"></div>
      <div class="thumb thumb--b" role="img" aria-label="Couple embracing portrait"></div>
      <div class="thumb thumb--more">•••</div>
    </div>
    <div class="card__cat">Wedding</div>
    <p class="card__excerpt">Pellentesque volutpat facilisis turpis fringilla tempus. Etiam orci nibh, tincidunt vel vulputate eu, ullamcorper in odio. In porta urna sed diam porttitor, sed malesuada quam facilisis. Praesent imperdiet metus sit amet augue imp[...]</p>
    <div class="card__likes"><svg width="14" height="12" viewBox="0 0 14 12"><path d="M7 11 1.6 5.6A3 3 0 0 1 7 2a3 3 0 0 1 5.4 3.6Z" fill="none" stroke="#b0103a" stroke-width="1.2"/></svg>1</div>
  </article>
</section>
<svg class="arrow arrow--prev" width="26" height="48" viewBox="0 0 26 48" aria-label="Previous"><path d="M24 1 2 24l22 23" fill="none" stroke="#888" stroke-width="2"/></svg>
<svg class="arrow arrow--next" width="26" height="48" viewBox="0 0 26 48" aria-label="Next"><path d="M2 1l22 23L2 47" fill="none" stroke="#888" stroke-width="2"/></svg>

<div class="rule" style="top:839px"></div>
<section class="ctas">
  <div class="cta" style="left:166px"><small>Book a</small><strong>Wedding</strong></div>
  <div class="cta" style="left:455px"><small>Book an</small><strong>Engagement</strong></div>
  <div class="cta" style="left:741px"><small>Book a</small><strong>Shoot</strong></div>
  <div class="cta" style="left:1029px"><small>Say</small><strong>hi!</strong></div>
</section>
<div class="rule" style="top:947px"></div>

<footer>
  <p class="copyright">Copyright © 2014 lumencraft. All rights reserved.</p>
  <div class="social social--foot" aria-label="Social links"><span></span><span></span><span></span><span></span><span></span><span></span></div>
</footer>
</body>
</html>
```